Social media app sign-up flow that asks users to give personal info and connect with other apps

Design an interactive, fun, and playful sign-up flow in which you are providing information about you, your interests, and connecting with different API plug-ins such as Plazabell, Workvane, Tunequill, etc. (using the brand palette attached).

Basic wireframe, and business requirements are also attached.

Target Market(s)

Gen Z + Millennials (ages 22-40)

Font styles to use
Sans Serif

Colors
fbed22
fbee3d
fbf289

Requirements
Must have
• Forms for users to submit their info. Follow the color palette attached.

Connect with Plazabell, Connect with Workvane, Connect with Tunequill, Connect with Gatherloop buttons
Nice to have
• I like the way you can use cards to submit your information for each category. Interactive card design for providing your info
Should not have
• Basic outdated designs, long forms

```html
<!DOCTYPE html>
<html lang="en">
<head>
<meta charset="utf-8">
<title>Tell me about you — sign-up flow, blue variations</title>
<link href="https://fonts.googleapis.com/css2?family=Comfortaa:wght@400;500;700&family=Source+Code+Pro:wght@400&display=swap" rel="stylesheet">
<style>
  :root{
    --page:#ffffff;
    --board:#f2f1ea;
    --screen:#f4f5f7;
    --slate:#5d6778;
    --slate-dark:#444a55;
    --mist:#b4b6ba;
    --haze:#b9c4d6;
    --gold:#cdb36d;
    --gold-dim:#9a8850;
    --sun:#fdc22d;
    --card:#ffffff;
    --ink:#2b2f36;
    --muted:#8a8f99;
    --field:#eaebef;
    --plazabell:#3b5a9a;
    --workvane:#3a9ad9;
  }
  *{box-sizing:border-box;margin:0;padding:0}
  html,body{width:747px;height:1200px;overflow:hidden;background:var(--page)}
  .board{width:1512px;height:2420px;transform:scale(.494);transform-origin:0 0;position:relative}
  .variant{position:absolute;width:678px}
  .variant-label{font-family:"Source Code Pro",monospace;font-size:22px;color:var(--ink);height:80px;padding-top:30px;margin-left:0}
  .stage{position:relative;width:678px;height:671px;background:var(--board)}
  .phone{position:absolute;top:55px;width:246px;height:546px;border-radius:22px;overflow:hidden;background:var(--screen);font-family:"Comfortaa",sans-serif;box-shadow:0 6px 18px rgba(40,45,60,.08)}
  .phone-menu{left:51px}
  .phone-detail{left:373px}
  .phone-art{position:absolute;inset:0;width:246px;height:546px}
  .back-arrow{position:absolute;left:12px;top:15px;width:12px;height:14px}
  .headline{position:absolute;left:20px;top:72px;font-size:28px;line-height:28px;color:#fff;font-weight:400}
  .category-grid{position:absolute;left:19px;top:157px;display:grid;grid-template-columns:98px 98px;column-gap:12px;row-gap:9px}
  .category-card{height:68px;background:var(--card);display:flex;align-items:center;justify-content:center;text-align:center;font-size:12px;line-height:12px;color:var(--ink);box-shadow:0 2px 6px rgba(40,45,60,.08)}
  .text-links{position:absolute;left:0;right:0;top:510px;display:flex;font-size:9px;color:var(--ink)}
  .text-links span{width:50%;text-align:center}
  .sheet{position:absolute;left:0;right:0;top:80px;bottom:0;background:var(--screen);border-radius:20px 20px 0 0}
  .back-link{position:absolute;left:22px;top:24px;font-size:12px;color:var(--ink)}
  .sheet-title{position:absolute;left:35px;top:58px;font-size:21px;line-height:23px;color:var(--ink)}
  .city-list{position:absolute;left:35px;top:128px;width:177px;list-style:none}
  .city-tag{height:29px;margin-bottom:4.5px;background:var(--gold);color:#fff;font-size:13px;display:flex;align-items:center;justify-content:space-between;padding:0 6px 0 11px}
  .city-tag b{font-weight:400;font-size:14px}
  .city-field{position:absolute;left:35px;top:268px;width:177px;height:29px;background:var(--field);border:1px solid #dcdee3;font-size:9px;color:var(--muted);padding:9px 11px}
  .connect-note{position:absolute;left:0;right:0;top:320px;text-align:center;font-size:9px;color:var(--ink)}
  .connect-row{position:absolute;left:45px;top:346px;display:flex;gap:23px}
  .connect-btn{width:68px;height:64px;color:#fff;display:flex;align-items:center;justify-content:center;font-size:10px;font-weight:700;box-shadow:0 3px 8px rgba(40,45,60,.15)}
  .connect-btn.plazabell{background:var(--plazabell)}
  .connect-btn.workvane{background:var(--workvane)}
</style>
</head>
<body>
<main class="board">

<!-- ===== Variant: Blue 1 ===== -->
<section class="variant" style="left:45px;top:0">
  <h2 class="variant-label" style="font-weight:400">Blue 1</h2>
  <div class="stage">
    <div class="phone phone-menu">
      <svg class="phone-art" viewBox="0 0 246 546">
        <path d="M0 0H246V160Q215 178 150 205L0 258Z" fill="var(--slate)"/>
        <path d="M246 378Q212 420 198 462Q135 478 124 546H246Z" fill="var(--sun)"/>
        <path d="M0 0H54Q54 46 0 56Z" fill="var(--gold)"/>
        <path d="M20 18L13 24L20 30" stroke="#fff" stroke-width="1.8" fill="none"/>
      </svg>
      <h1 class="headline">Tell me<br>about you</h1>
      <div class="category-grid">
        <div class="category-card">Places<br>I've Lived</div><div class="category-card">Schools I've<br>Attented</div>
        <div class="category-card">Where<br>I worked</div><div class="category-card">People<br>I Know</div>
        <div class="category-card">Events I've<br>Attended</div><div class="category-card">Events I'm<br>Attending</div>
        <div class="category-card">Music I<br>Love</div><div class="category-card">Teams<br>I love</div>
      </div>
      <div class="text-links"><span>Text Link 1</span><span>Text Link 2</span></div>
    </div>
    <div class="phone phone-detail">
      <svg class="phone-art" viewBox="0 0 246 546">
        <rect width="246" height="100" fill="var(--slate-dark)"/>
        <path d="M0 0H54Q54 46 0 56Z" fill="var(--gold-dim)"/>
        <path d="M20 18L13 24L20 30" stroke="#c9c9c9" stroke-width="1.8" fill="none"/>
      </svg>
      <div class="sheet">
        <span class="back-link">‹ back</span>
        <h3 class="sheet-title" style="font-weight:400">Places<br>I've Lived</h3>
        <ul class="city-list"><li class="city-tag">Rome<b>×</b></li><li class="city-tag">Bruxelles<b>×</b></li><li class="city-tag">Madrid<b>×</b></li></ul>
        <div class="city-field">Type a city</div>
        <p class="connect-note">or simply connect with</p>
        <div class="connect-row"><span class="connect-btn plazabell">Plazabell</span><span class="connect-btn workvane">Workvane</span></div>
      </div>
    </div>
  </div>
</section>

<!-- ===== Variant: Blue 1b ===== -->
<section class="variant" style="left:789px;top:0">
  <h2 class="variant-label" style="font-weight:400">Blue 1b</h2>
  <div class="stage">
    <div class="phone phone-menu">
      <svg class="phone-art" viewBox="0 0 246 546">
        <path d="M246 150V230Q180 240 0 280V250Z" fill="var(--haze)"/>
        <path d="M0 0H246V160Q215 178 150 205L0 258Z" fill="var(--slate)"/>
        <path d="M246 378Q212 420 198 462Q135 478 124 546H246Z" fill="var(--sun)"/>
        <path d="M0 0H54Q54 46 0 56Z" fill="var(--gold)"/>
        <path d="M20 18L13 24L20 30" stroke="#fff" stroke-width="1.8" fill="none"/>
      </svg>
      <h1 class="headline">Tell me<br>about you</h1>
      <div class="category-grid">
        <div class="category-card">Places<br>I've Lived</div><div class="category-card">Schools I've<br>Attented</div>
        <div class="category-card">Where<br>I worked</div><div class="category-card">People<br>I Know</div>
        <div class="category-card">Events I've<br>Attended</div><div class="category-card">Events I'm<br>Attending</div>
        <div class="category-card">Music I<br>Love</div><div class="category-card">Teams<br>I love</div>
      </div>
      <div class="text-links"><span>Text Link 1</span><span>Text Link 2</span></div>
    </div>
    <div class="phone phone-detail">
      <svg class="phone-art" viewBox="0 0 246 546">
        <rect width="246" height="100" fill="var(--slate-dark)"/>
        <path d="M0 0H54Q54 46 0 56Z" fill="var(--gold-dim)"/>
        <path d="M20 18L13 24L20 30" stroke="#c9c9c9" stroke-width="1.8" fill="none"/>
      </svg>
      <div class="sheet">
        <span class="back-link">‹ back</span>
        <h3 class="sheet-title" style="font-weight:400">Places<br>I've Lived</h3>
        <ul class="city-list"><li class="city-tag">Rome<b>×</b></li><li class="city-tag">Bruxelles<b>×</b></li><li class="city-tag">Madrid<b>×</b></li></ul>
        <div class="city-field">Type a city</div>
        <p class="connect-note">or simply connect with</p>
        <div class="connect-row"><span class="connect-btn plazabell">Plazabell</span><span class="connect-btn workvane">Workvane</span></div>
      </div>
    </div>
  </div>
</section>

<!-- ===== Variant: Blue 2 ===== -->
<section class="variant" style="left:45px;top:810px">
  <h2 class="variant-label" style="font-weight:400">Blue 2</h2>
  <div class="stage">
    <div class="phone phone-menu">
      <svg class="phone-art" viewBox="0 0 246 546">
        <circle cx="80" cy="85" r="118" fill="var(--slate)"/>
        <circle cx="225" cy="530" r="118" fill="var(--sun)"/>
        <path d="M0 0H54Q54 46 0 56Z" fill="var(--gold)"/>
        <path d="M20 18L13 24L20 30" stroke="#fff" stroke-width="1.8" fill="none"/>
      </svg>
      <h1 class="headline">Tell me<br>about you</h1>
      <div class="category-grid">
        <div class="category-card">Places<br>I've Lived</div><div class="category-card">Schools I've<br>Attented</div>
        <div class="category-card">Where<br>I worked</div><div class="category-card">People<br>I Know</div>
        <div class="category-card">Events I've<br>Attended</div><div class="category-card">Events I'm<br>Attending</div>
        <div class="category-card">Music I<br>Love</div><div class="category-card">Teams<br>I love</div>
      </div>
      <div class="text-links"><span>Text Link 1</span><span>Text Link 2</span></div>
    </div>
    <div class="phone phone-detail">
      <svg class="phone-art" viewBox="0 0 246 546">
        <rect width="246" height="100" fill="var(--mist)"/>
        <circle cx="80" cy="85" r="108" fill="var(--slate-dark)"/>
        <path d="M0 0H54Q54 46 0 56Z" fill="var(--gold-dim)"/>
        <path d="M20 18L13 24L20 30" stroke="#c9c9c9" stroke-width="1.8" fill="none"/>
      </svg>
      <div class="sheet">
        <span class="back-link">‹ back</span>
        <h3 class="sheet-title" style="font-weight:400">Places<br>I've Lived</h3>
        <ul class="city-list"><li class="city-tag">Rome<b>×</b></li><li class="city-tag">Bruxelles<b>×</b></li><li class="city-tag">Madrid<b>×</b></li></ul>
        <div class="city-field">Type a city</div>
        <p class="connect-note">or simply connect with</p>
        <div class="connect-row"><span class="connect-btn plazabell">Plazabell</span><span class="connect-btn workvane">Workvane</span></div>
      </div>
    </div>
  </div>
</section>

<!-- ===== Variant: Blue 3 ===== -->
<section class="variant" style="left:789px;top:810px">
  <h2 class="variant-label" style="font-weight:400">Blue 3</h2>
  <div class="stage">
    <div class="phone phone-menu">
      <svg class="phone-art" viewBox="0 0 246 546">
        <path d="M0 0H150Q160 45 180 90Q190 140 150 160Q80 180 0 170Z" fill="var(--slate)"/>
        <path d="M246 450Q230 480 195 495Q140 500 120 515Q115 540 160 540Q230 535 246 505Z" fill="var(--sun)"/>
        <path d="M0 0H54Q54 46 0 56Z" fill="var(--gold)"/>
        <path d="M20 18L13 24L20 30" stroke="#fff" stroke-width="1.8" fill="none"/>
      </svg>
      <h1 class="headline">Tell me<br>about you</h1>
      <div class="category-grid">
        <div class="category-card">Places<br>I've Lived</div><div class="category-card">Schools I've<br>Attented</div>
        <div class="category-card">Where<br>I worked</div><div class="category-card">People<br>I Know</div>
        <div class="category-card">Events I've<br>Attended</div><div class="category-card">Events I'm<br>Attending</div>
        <div class="category-card">Music I<br>Love</div><div class="category-card">Teams<br>I love</div>
      </div>
      <div class="text-links"><span>Text Link 1</span><span>Text Link 2</span></div>
    </div>
    <div class="phone phone-detail">
      <svg class="phone-art" viewBox="0 0 246 546">
        <rect width="246" height="100" fill="var(--mist)"/>
        <path d="M0 0H145Q155 45 175 100H0Z" fill="var(--slate-dark)"/>
        <path d="M0 0H54Q54 46 0 56Z" fill="var(--gold-dim)"/>
        <path d="M20 18L13 24L20 30" stroke="#c9c9c9" stroke-width="1.8" fill="none"/>
      </svg>
      <div class="sheet">
        <span class="back-link">‹ back</span>
        <h3 class="sheet-title" style="font-weight:400">Places<br>I've Lived</h3>
        <ul class="city-list"><li class="city-tag">Rome<b>×</b></li><li class="city-tag">Bruxelles<b>×</b></li><li class="city-tag">Madrid<b>×</b></li></ul>
        <div class="city-field">Type a city</div>
        <p class="connect-note">or simply connect with</p>
        <div class="connect-row"><span class="connect-btn plazabell">Plazabell</span><span class="connect-btn workvane">Workvane</span></div>
      </div>
    </div>
  </div>
</section>

<!-- ===== Variant: Blue 4 ===== -->
<section class="variant" style="left:45px;top:1620px">
  <h2 class="variant-label" style="font-weight:400">Blue 4</h2>
  <div class="stage">
    <div class="phone phone-menu">
      <svg class="phone-art" viewBox="0 0 246 546">
        <defs>
          <linearGradient id="mist-fade" x1="0" y1="1" x2="0.3" y2="0"><stop offset="0" stop-color="#8d96a6"/><stop offset="1" stop-color="#eef0f3"/></linearGradient>
          <linearGradient id="sun-fade" x1="0" y1="0" x2="0" y2="1"><stop offset="0" stop-color="#fbf289" stop-opacity=".3"/><stop offset="1" stop-color="var(--sun)" stop-opacity=".6"/></linearGradient>
        </defs>
        <circle cx="80" cy="85" r="118" fill="url(#mist-fade)"/>
        <circle cx="225" cy="530" r="118" fill="url(#sun-fade)"/>
        <path d="M0 0H54Q54 46 0 56Z" fill="var(--gold)"/>
        <path d="M20 18L13 24L20 30" stroke="#fff" stroke-width="1.8" fill="none"/>
      </svg>
      <h1 class="headline">Tell me<br>about you</h1>
      <div class="category-grid">
        <div class="category-card">Places<br>I've Lived</div><div class="category-card">Schools I've<br>Attented</div>
        <div class="category-card">Where<br>I worked</div><div class="category-card">People<br>I Know</div>
        <div class="category-card">Events I've<br>Attended</div><div class="category-card">Events I'm<br>Attending</div>
        <div class="category-card">Music I<br>Love</div><div class="category-card">Teams<br>I love</div>
      </div>
      <div class="text-links"><span>Text Link 1</span><span>Text Link 2</span></div>
    </div>
    <div class="phone phone-detail">
      <svg class="phone-art" viewBox="0 0 246 546">
        <rect width="246" height="100" fill="var(--mist)"/>
        <circle cx="80" cy="85" r="108" fill="#8e939c"/>
        <path d="M0 0H54Q54 46 0 56Z" fill="var(--gold-dim)"/>
        <path d="M20 18L13 24L20 30" stroke="#c9c9c9" stroke-width="1.8" fill="none"/>
      </svg>
      <div class="sheet">
        <span class="back-link">‹ back</span>
        <h3 class="sheet-title" style="font-weight:400">Places<br>I've Lived</h3>
        <ul class="city-list"><li class="city-tag">Rome<b>×</b></li><li class="city-tag">Bruxelles<b>×</b></li><li class="city-tag">Madrid<b>×</b></li></ul>
        <div class="city-field">Type a city</div>
        <p class="connect-note">or simply connect with</p>
        <div class="connect-row"><span class="connect-btn plazabell">Plazabell</span><span class="connect-btn workvane">Workvane</span></div>
      </div>
    </div>
  </div>
</section>

<!-- ===== Variant: Blue 5 ===== -->
<section class="variant" style="left:789px;top:1620px">
  <h2 class="variant-label" style="font-weight:400">Blue 5</h2>
  <div class="stage">
    <div class="phone phone-menu">
      <svg class="phone-art" viewBox="0 0 246 546">
        <path d="M0 0H246V250L0 292Z" fill="var(--slate)"/>
        <path d="M246 330L0 445V546H246Z" fill="var(--sun)"/>
        <path d="M0 0H54Q54 46 0 56Z" fill="var(--gold)"/>
        <path d="M20 18L13 24L20 30" stroke="#fff" stroke-width="1.8" fill="none"/>
      </svg>
      <h1 class="headline">Tell me<br>about you</h1>
      <div class="category-grid">
        <div class="category-card">Places<br>I've Lived</div><div class="category-card">Schools I've<br>Attented</div>
        <div class="category-card">Where<br>I worked</div><div class="category-card">People<br>I Know</div>
        <div class="category-card">Events I've<br>Attended</div><div class="category-card">Events I'm<br>Attending</div>
        <div class="category-card">Music I<br>Love</div><div class="category-card">Teams<br>I love</div>
      </div>
      <div class="text-links"><span>Text Link 1</span><span>Text Link 2</span></div>
    </div>
    <div class="phone phone-detail">
      <svg class="phone-art" viewBox="0 0 246 546">
        <rect width="246" height="100" fill="var(--slate-dark)"/>
        <path d="M0 0H54Q54 46 0 56Z" fill="var(--gold-dim)"/>
        <path d="M20 18L13 24L20 30" stroke="#c9c9c9" stroke-width="1.8" fill="none"/>
      </svg>
      <div class="sheet">
        <span class="back-link">‹ back</span>
        <h3 class="sheet-title" style="font-weight:400">Places<br>I've Lived</h3>
        <ul class="city-list"><li class="city-tag">Rome<b>×</b></li><li class="city-tag">Bruxelles<b>×</b></li><li class="city-tag">Madrid<b>×</b></li></ul>
        <div class="city-field">Type a city</div>
        <p class="connect-note">or simply connect with</p>
        <div class="connect-row"><span class="connect-btn plazabell">Plazabell</span><span class="connect-btn workvane">Workvane</span></div>
      </div>
    </div>
  </div>
</section>

</main>
</body>
</html>
```